Keys to business success

I love the principles of a book called "The quiet art of tending small gardens". I use the principles all the time at work. I'd like a poster made (map or web style design) to capture the books reminders. You can see a very basic verison of the design i'm looking for attached below "project summary".I've attached a word document of the text to include. Ive also attached two examples of the types of designs i'm looking for. The design will have to look modern and clear when printed on an 45.7 x 61 cm canvas.

Target Market(s)

Buisness people
Motivation

Industry/Entity Type

Business

Font styles to use
Serif

Requirements
Must have
• Web or map-like designs
• All 30 of the principles: 3 fonts (Title, sub-title and principles). The choice of fonts is up to the designer. No numbers for the principles.
• Professional feel
Nice to have
• Halos around phrases
Should not have
• No straight lines or ridgid concepts

```html
<!DOCTYPE html>
<html lang="en">
<head>
<meta charset="utf-8">
<title>30 Principles – The Quiet Art of Tending Small Gardens</title>
<link href="https://fonts.googleapis.com/css2?family=Jost:wght@500;600&family=Oswald:wght@600;700&display=swap" rel="stylesheet">
<style>
  :root{
    --sky:#00c6fb;
    --navy:#0537b4;
    --title-blue:#0a3ec4;
    --rule:#1f4fe0;
    --white:#ffffff;
  }
  html,body{margin:0;padding:0;overflow:hidden;background:var(--sky);}
  .poster{position:relative;width:1200px;height:899px;background:var(--sky);overflow:hidden;font-family:"Jost",sans-serif;}
  .shapes{position:absolute;inset:0;}
  .hex-label{position:absolute;color:var(--white);font-weight:600;font-size:18.5px;line-height:0.98;text-transform:uppercase;letter-spacing:0.1px;}
  .hex-label--fundamentals{left:351px;top:182px;}
  .hex-label--thinking{left:703px;top:191px;}
  .hex-label--liking{left:379px;top:672px;}
  .hex-label--leader{left:724px;top:681px;}
  .core-title{position:absolute;left:455px;top:372px;width:278px;text-align:center;color:var(--title-blue);font-family:"Oswald",sans-serif;text-transform:uppercase;}
  .core-title__kicker{display:block;font-size:27px;font-weight:600;line-height:1;letter-spacing:0.5px;}
  .core-title__main{display:block;font-size:35px;font-weight:700;line-height:0.98;letter-spacing:-0.5px;margin-top:2px;}
  .principles{position:absolute;margin:0;padding:0;list-style:none;color:var(--white);font-size:12.4px;font-weight:500;white-space:nowrap;}
  .principles li{border-bottom:1px solid var(--rule);}
  .principles--right{border-left:1px solid var(--rule);}
  .principles--right li{padding-left:10px;}
  .principles--left{border-right:1px solid var(--rule);text-align:right;}
  .principles--left li{padding-right:3px;}
  .principles--fundamentals{left:15px;top:185px;width:299px;border-top:1px solid var(--rule);}
  .principles--fundamentals li{line-height:22px;}
  .principles--thinking{left:860px;top:70px;width:322px;border-top:1px solid var(--rule);}
  .principles--thinking li{line-height:17.3px;}
  .principles--liking{left:15px;top:613px;width:299px;border-top:1px solid var(--rule);}
  .principles--liking li{line-height:18.5px;}
  .principles--leader{left:860px;top:562px;width:322px;border-top:1px solid var(--rule);}
  .principles--leader li{line-height:18.9px;}
</style>
</head>
<body>
<main class="poster">
  <svg class="shapes" width="1200" height="899" viewBox="0 0 1200 899" aria-hidden="true">
    <g class="connectors" stroke="var(--navy)" stroke-width="1" stroke-dasharray="2 2" fill="none">
      <line x1="455" y1="292" x2="510" y2="346"/>
      <line x1="718" y1="290" x2="666" y2="340"/>
      <line x1="460" y1="601" x2="512" y2="551"/>
      <line x1="715" y1="605" x2="666" y2="574"/>
      <line x1="314" y1="217" x2="333" y2="217" stroke-dasharray="none" stroke="var(--rule)"/>
      <line x1="845" y1="218" x2="860" y2="218" stroke-dasharray="none" stroke="var(--rule)"/>
      <line x1="314" y1="697" x2="333" y2="697" stroke-dasharray="none" stroke="var(--rule)"/>
      <line x1="845" y1="697" x2="860" y2="697" stroke-dasharray="none" stroke="var(--rule)"/>
    </g>
    <g class="topic-hexes" fill="var(--navy)">
      <polygon points="417,122 501,169 501,265 417,312 333,265 333,169"/>
      <polygon points="761,122 845,170 845,265 761,313 677,265 677,170"/>
      <polygon points="417,600 501,648 501,746 417,794 333,746 333,648"/>
      <polygon points="761,600 845,648 845,746 761,794 677,746 677,648"/>
    </g>
    <polygon class="core-hex" points="593,298 732,378 732,540 593,619 455,540 455,378" fill="var(--white)" stroke="var(--navy)" stroke-width="4"/>
  </svg>

  <h1 class="core-title">
    <span class="core-title__kicker">30 Principles</span>
    <span class="core-title__main">The Quiet Art<br>of Tending<br>Small Gardens</span>
  </h1>

  <h2 class="hex-label hex-label--fundamentals">Fundamental<br>Techniques In<br>Handling<br>People</h2>
  <h2 class="hex-label hex-label--thinking">Win People<br>To Yourway<br>Of Thinking</h2>
  <h2 class="hex-label hex-label--liking">Making<br>People<br>Like You</h2>
  <h2 class="hex-label hex-label--leader">Being A<br>Leader</h2>

  <ul class="principles principles--left principles--fundamentals">
    <li>Don't Criticize, Condemn or Complain</li>
    <li>Give Honest, Sincere, Appreciation</li>
    <li>Arouse In The Other Person An Eager Want</li>
  </ul>

  <ul class="principles principles--right principles--thinking">
    <li>The Only Way To Get The Best Of AnArgumentIs<br>To Avoid It</li>
    <li>Show Respect For The Other Person's Opinion.</li>
    <li>Never Say, "You're Wrong."</li>
    <li>If You Are Wrong Admit It Quickly And Emphatically</li>
    <li>Begin In A Friendly Manner</li>
    <li>Get The Other Person Saying "Yes, Yes"</li>
    <li>Let The Other Person Do A Great Deal Of The Talking</li>
    <li>Let The Other Person Feel That The Idea Is His<br>Or Hers</li>
    <li>Try Honestly To See Things From The Other<br>Person's Point Of View</li>
    <li>Be Sympathetic With The Other Person's Ideas<br>And Desires</li>
    <li>Appeal To The Nobler Motives</li>
    <li>Dramatize Your Ideas</li>
    <li>Throw Down A Challenge</li>
  </ul>

  <ul class="principles principles--left principles--liking">
    <li>Become Genuinely Interested In Other People</li>
    <li>Smile</li>
    <li>A Person's Name Is To That Person The Sweetest<br>And Most Important Sound</li>
    <li>Be A Good Listener. Encourage Others<br>To Talk About Themselves</li>
    <li>Talk In Terms Of The Other Person's Interests</li>
    <li>Make The Other Person Feel Important<br>- And Do It Sincerely</li>
  </ul>

  <ul class="principles principles--right principles--leader">
    <li>Begin With Praise And Honest Appreciation</li>
    <li>Call Attention To People's Mistakes Indirectly</li>
    <li>Talk About Your Own Mistakes Before Criticizing<br>The Other Person</li>
    <li>Ask Questions Instead Of Giving Direct Orders</li>
    <li>Let The Other Person Save Face</li>
    <li>Praise The Slightest Improvement And Praise<br>Every Improvement.</li>
    <li>Give The Other Person A Fine Reputation To<br>Live Up To</li>
    <li>Use Encouragement. Make The Fault Seem<br>Easy To Correct</li>
    <li>Make The Other Person Happy About Doing<br>The Thing You Suggest</li>
  </ul>
</main>
</body>
</html>
```